Business Card Design Project - IT Company

Kestrafield Information Technology Solutions
We are an Information Technology Company. We provide computer services to commercial companies. We would like a new card full color front and back with bleeding edge.
We have a logo that you can use or if you want to come up with a new logo that is fine too.
Our colors are mostly Maroon and black but be creative.
Sample Information
Brent R Okafor
4812 W Saguaro Ridge Drive
Suite 600
Phoenix, AZ 85016
O: 602.914.2037
C: 602.468.1290
24/7: 888.914.2037
bokafor@kestrafield.example
www.kestrafield.example
Target Market(s)
Business of all sizes
Industry/Entity Type
Computer
Requirements
Must have
- Bleeding edge
full color on both sides

```html
<!DOCTYPE html>
<html lang="en">
<head>
<meta charset="utf-8">
<title>Kestrafield Business Card</title>
<link rel="stylesheet" href="https://fonts.googleapis.com/css2?family=Noto+Serif:wght@400&family=Source+Sans+3:wght@400&display=swap">
<style>
  :root {
    --page: #ffffff;
    --card: #0d0a0a;
    --maroon: #b5222b;
    --wordmark-grey: #6b686a;
    --text-light: #f2f2f2;
    --text-muted: #9a9698;
    --text-dim: #6f6b6c;
  }
  * { margin: 0; padding: 0; box-sizing: border-box; }
  html, body {
    width: 1200px;
    height: 686px;
    overflow: hidden;
    background: var(--page);
  }
  .card {
    position: absolute;
    background: var(--card);
    font-family: "Source Sans 3", "Myriad Pro", sans-serif;
  }
  .card--front { left: 29px; top: 48px; width: 548px; height: 305px; }
  .card--back  { left: 638px; top: 370px; width: 557px; height: 311px; }

  .wordmark {
    position: absolute;
    font-family: "Source Sans 3", sans-serif;
    font-weight: 400;
    color: var(--wordmark-grey);
    letter-spacing: 0.5px;
    line-height: 1;
    white-space: nowrap;
  }
  .card--front .wordmark {
    left: 0; right: 0; top: 8px;
    text-align: center;
    font-size: 38px;
  }
  .card--back .wordmark {
    left: 25px; top: 10px;
    font-size: 36px;
  }
  .holder-name {
    position: absolute;
    left: 0; right: 0; top: 233px;
    text-align: center;
    font-family: "Noto Serif", serif;
    font-size: 18px;
    color: var(--text-light);
  }
  .tagline {
    position: absolute;
    font-family: "Noto Serif", serif;
    color: var(--text-muted);
    white-space: nowrap;
  }
  .card--front .tagline {
    left: 0; right: 0; top: 279px;
    text-align: center;
    font-size: 15px;
  }
  .card--back .tagline {
    left: 25px; top: 43px;
    font-size: 11px;
    color: #8a8687;
  }
  .rule {
    position: absolute;
    left: 25px; top: 56px;
    width: 523px; height: 2px;
    background: var(--maroon);
  }
  .contact {
    position: absolute;
    font-size: 15.5px;
    color: var(--text-dim);
    line-height: 1;
  }
  .contact p { position: absolute; white-space: nowrap; }
  .contact--address { left: 30px; top: 0; }
  .contact--address p { left: 0; }
  .contact--phones { right: 34px; top: 0; }
  .contact--phones p { right: 0; text-align: right; }
  .contact--online { left: 0; top: 0; width: 100%; }
  .contact--online p { transform: translateX(-50%); }
</style>
</head>
<body>
  <section class="card card--front" aria-label="Card front">
    <div class="wordmark">KESTRAFIELD</div>
    <div class="holder-name">Brent R Okafor</div>
    <div class="tagline">Information Technology Solutions</div>
  </section>

  <section class="card card--back" aria-label="Card back">
    <div class="wordmark">KESTRAFIELD</div>
    <div class="tagline">Information Technology Solutions</div>
    <div class="rule"></div>

    <div class="contact contact--address">
      <p style="top:83px">4812 W Saguaro Ridge Drive</p>
      <p style="top:108px">Suite 600</p>
    </div>

    <div class="contact contact--phones">
      <p style="top:79px">Phoenix, AZ 85016</p>
      <p style="top:102px">O: 602.914.2037</p>
      <p style="top:127px">C: 602.468.1290</p>
      <p style="top:154px">24/7: 888.914.2037</p>
    </div>

    <div class="contact contact--online">
      <p style="left:156px; top:283px">bokafor@kestrafield.example</p>
      <p style="left:398px; top:283px">www.kestrafield.example</p>
    </div>
  </section>
</body>
</html>
```